Need website redesign!

I have a site, www.pinebrookfitcamp.com

I am looking to have it redesigned to make it simpler, and encourage people who hit the home page to click on a service, opt in, or contact me for more info. Having a video front and center with icons representing the services we offer around it may be a good idea, but I am open to YOUR design. Conversion is my goal. I want it to be friendly, but convey the fun and ENERGY of my bootcamp. Scrolling pics on home page so people can get a feel for our bootcamp is recommended as well.

```html
<!DOCTYPE html>
<html lang="en">
<head>
<meta charset="utf-8">
<title>Pinebrook Fit Camp</title>
<link href="https://fonts.googleapis.com/css2?family=Mulish:wght@400;600;700;800&display=swap" rel="stylesheet">
<style>
:root{
  --black:#000;
  --dark:#1b1b1b;
  --red:#e3141b;
  --red-dark:#c80d12;
  --blue:#146fa6;
  --blue-text:#1d6fae;
  --white:#fff;
  --grey-text:#555;
  --border:#dcdcdc;
  --btn-dark:#3a3a3a;
}
*{margin:0;padding:0;box-sizing:border-box}
html,body{width:927px;height:1200px;overflow:hidden}
body{font-family:"Mulish",sans-serif;background:var(--white);position:relative;color:var(--grey-text)}
.abs{position:absolute}
.site-header{left:0;top:0;width:927px;height:100px;background:var(--black)}
.logo{left:60px;top:18px;width:120px;color:var(--white);font-weight:800;font-size:17px;line-height:19px;text-transform:uppercase}
.logo small{display:block;font-size:5px;line-height:8px;font-weight:600;letter-spacing:.3px;margin-top:4px}
.nav{left:424px;top:0;display:flex;height:71px}
.nav a{color:var(--white);text-decoration:none;font-size:11.5px;padding:41px 18px 0;height:71px;display:block}
.nav a.active{background:var(--red);border-bottom:5px solid var(--white);padding:41px 20px 0}
.red-band{left:0;top:325px;width:927px;height:233px;background:linear-gradient(var(--red),var(--red-dark))}
.hero{left:57px;top:82px;width:813px;height:288px;border:4px solid var(--white);background:linear-gradient(120deg,#8a7d75,#3d3a3a 55%,#2a2a2a);box-shadow:0 0 0 1px #ccc}
.dots{left:432px;top:325px;display:flex;gap:5px}
.dots span{width:11px;height:11px;border-radius:50%;background:#bbb}
.dots span:first-child{background:var(--white)}
.optin{left:598px;top:116px;width:240px;height:220px;background:var(--blue);border:3px solid var(--white);padding:10px 15px 0;color:var(--white)}
.optin h2{font-weight:600;font-size:15px;line-height:20px}
.optin .field{background:var(--white);color:#666;font-size:10px;height:27px;padding:8px 11px;margin-top:12px}
.optin .field+.field{margin-top:6px}
.optin .go{margin:6px 0 0 auto;width:122px;height:27px;background:var(--btn-dark);font-size:10px;text-align:center;padding-top:8px}
.optin p{font-style:italic;font-size:8.5px;line-height:14px;margin-top:8px;width:195px;text-transform:uppercase}
.intro-photo{left:57px;top:398px;width:208px;height:139px;border:3px solid var(--white);background:linear-gradient(90deg,#5a6066,#30363a)}
.intro{left:290px;top:396px;width:578px;color:var(--white)}
.intro h1{font-weight:600;font-size:16.5px;margin-bottom:9px}
.intro p{font-size:9.5px;line-height:16.4px}
.btn-blue{background:var(--blue);color:var(--white);font-size:10px;text-align:center;display:block}
.intro .btn-blue{width:117px;height:30px;padding-top:10px;margin-top:13px}
.panel{border:1px solid var(--border);background:var(--white)}
.panel-head{height:31px;color:var(--white);font-size:17px;padding:6px 12px;font-weight:600;position:relative}
.panel-head.black{background:var(--black)}
.panel-head.red{background:var(--red)}
.classes{left:57px;top:588px;width:465px;height:214px}
.col{position:absolute;top:44px;width:225px;font-size:9.6px}
.col h3{color:var(--red);font-weight:600;font-size:11.5px;line-height:16px;margin-bottom:7px}
.col p{line-height:20px}
.members{position:absolute;left:68px;top:168px;color:var(--blue-text);font-size:11px;padding-top:8px;font-weight:600}
.classes .btn-blue{position:absolute;left:255px;top:168px;width:117px;height:30px;padding-top:9px}
.video{left:544px;top:588px;width:326px;height:214px}
.player{position:absolute;left:18px;top:40px;width:289px;height:159px;background:var(--black)}
.player .frame{position:absolute;left:98px;top:0;width:92px;height:144px;background:linear-gradient(#e4a970,#3a3a3a)}
.player .bar{position:absolute;left:0;bottom:0;width:100%;height:15px;background:#151515}
.player .progress{position:absolute;left:0;bottom:14px;width:100%;height:2px;background:#444}
.player .progress i{display:block;width:16px;height:2px;background:var(--red)}
.services{left:57px;top:820px;width:535px;height:226px}
.arrows{position:absolute;right:14px;top:8px}
.svc-photo{position:absolute;left:15px;top:48px;width:187px;height:161px;background:linear-gradient(90deg,#7b7f82,#2f3f5f);border:1px solid var(--border)}
.svc-text{position:absolute;left:216px;top:44px;width:292px;font-size:9.6px;line-height:16.4px}
.svc-text h3{color:var(--blue-text);font-size:14px;font-weight:600;margin-bottom:3px}
.btn-dark{position:absolute;left:216px;top:180px;width:117px;height:30px;background:var(--btn-dark);color:var(--white);font-size:10px;text-align:center;padding-top:9px}
.locations{left:614px;top:820px;width:256px;height:226px}
.loc{position:absolute;left:16px;top:44px;width:230px;font-size:9.6px;line-height:16.4px}
.loc h3{color:var(--blue-text);font-size:10.8px;font-weight:600;margin-bottom:1px}
.loc .and{color:var(--red);display:block;margin:1px 0 2px}
.like{position:absolute;left:17px;top:184px;width:161px;height:27px;background:#3c5aa0;border:2px solid #6d86c1;border-radius:2px;color:var(--white);font-weight:700;font-size:12px;display:flex;align-items:center;gap:7px;padding-left:13px;letter-spacing:-.3px}
.like i{width:13px;height:13px;border:2px solid var(--white);border-radius:50%}
.footer{left:0;top:1092px;width:927px;height:108px;background:var(--dark)}
.tagline{left:57px;top:1061px;width:813px;height:63px;background:var(--blue);color:var(--white);font-size:13.6px;text-align:center;line-height:19.5px;padding-top:11px}
.foot-links{left:56px;top:1137px;color:var(--white);font-size:9.6px;word-spacing:2px}
.foot-links span{margin:0 10px}
.copy{left:56px;top:1159px;color:#ccc;font-size:9.6px;line-height:14.5px}
.connect{left:712px;top:1151px;display:flex;align-items:center;gap:5px;color:var(--white);font-size:9.6px}
.connect .lbl{margin-right:7px}
.connect i{width:25px;height:25px;border-radius:50%;border:2px solid #aaa}
</style>
</head>
<body>
<header class="site-header abs">
  <div class="logo abs">Pinebrook<br>Fit Camp<small>pinebrookfitcamp.com</small></div>
  <nav class="nav abs">
    <a class="active">Home</a><a>Services</a><a>Classes</a><a>About Us</a><a>FAQ's</a><a>Contact Us</a>
  </nav>
</header>

<div class="red-band abs"></div>

<div class="hero abs" role="img" aria-label="Slideshow photo of bootcamp members training with battle ropes in the gym"></div>
<div class="dots abs"><span></span><span></span><span></span><span></span></div>

<form class="optin abs">
  <h2>Leave your email for a FREE week of bootcamp,<br>NO OBLIGATION</h2>
  <div class="field">Enter Name</div>
  <div class="field">Enter Email</div>
  <div class="go">GET STARTED NOW</div>
  <p>*Spam free zone.your email is<br>safe &amp; secure.</p>
</form>

<div class="intro-photo abs" role="img" aria-label="Photo of a bootcamp class doing floor exercises on mats"></div>
<section class="intro abs">
  <h1>WHAT IS PINEBROOK FIT CAMP?</h1>
  <p>Pine County&amp; Brook County Pinebrook Fit Camp locations Comprise a high energy fitness program that includes challenging workouts, camaraderie, positive-motivation. Pinebrook Fit Camp was started by longtime Pine County, Maryland resident Dale Morrow. Dale has been training individuals and small groups for more than 15 years and after one too many WET and COLD outdoor bootcamp workouts, Dale decided that INSIDE was the way to go.</p>
  <span class="btn-blue">GET STARTED NOW</span>
</section>

<section class="classes panel abs">
  <div class="panel-head black">CLASSES</div>
  <div class="col" style="left:15px">
    <h3>Fernwood/Oakridge Location (morning only)</h3>
    <p>M-F: 5:30am, 6:30am<br>M, W, F:&nbsp; 7:30a, 9:30am<br>Yoga: Monday 7pm, Wednesday 6pm<br>Dance Cardio: Tuesday 6pm, Thursday 7pm</p>
  </div>
  <div class="col" style="left:238px">
    <h3>Ridgefield Location (morning, evening, weekends!)</h3>
    <p>Bootcamp: Morning: M-F 5:30am<br>Eve: M,W 6:30pm Tues, Thurs 6:15pm<br>Weekends: Sat 8am, 9am<br>Kids Sports/Agility: M,W 4pm, 5:15pm</p>
  </div>
  <div class="members">FOR CURRENT MEMBERS ONLY</div>
  <span class="btn-blue">BOOK NOW</span>
</section>

<section class="video panel abs">
  <div class="panel-head black">WATCH A VIDEO</div>
  <div class="player">
    <div class="frame" role="img" aria-label="Video still of the coach introducing the bootcamp"></div>
    <div class="progress"><i></i></div>
    <div class="bar">
      <svg width="289" height="15"><rect x="10" y="4" width="2" height="7" fill="#ccc"/><rect x="14" y="4" width="2" height="7" fill="#ccc"/><path d="M28 6h3l3-3v9l-3-3h-3z" fill="#ccc"/><circle cx="241" cy="7.5" r="2.5" fill="#ccc"/><circle cx="253" cy="7.5" r="3" fill="none" stroke="#ccc"/><rect x="264" y="4" width="8" height="6" fill="none" stroke="#ccc"/><rect x="277" y="4" width="7" height="7" fill="none" stroke="#ccc" stroke-dasharray="3 2"/></svg>
    </div>
  </div>
</section>

<section class="services panel abs">
  <div class="panel-head red">OUR SERVICES
    <svg class="arrows" width="34" height="14" viewBox="0 0 34 14"><path d="M7 1L1 7l6 6M27 1l6 6-6 6" fill="none" stroke="#fff" stroke-width="1.6"/></svg>
  </div>
  <div class="svc-photo" role="img" aria-label="Photo of a trainer coaching a client on suspension straps"></div>
  <div class="svc-text">
    <h3>PERSONAL TRAINING</h3>
    If you're in Western Pine County, Harlow City, Ashbury, Ridgefield, Millbrook or Kingsford, come and check out Pinebrook Fit Camp for a workout program designed to burn fat and get you into the best shape of your life!<br>Our fun, effective workouts are designed to give you the MAXIMUM results in the MINIMUM amount of time.
  </div>
  <span class="btn-dark">READ MORE</span>
</section>

<section class="locations panel abs">
  <div class="panel-head red">OUR LOCATIONS</div>
  <div class="loc">
    <h3>PINEBROOK FIT CAMP</h3>
    Millbrook Martial Arts Studio<br>1180 Harlow Lane Fernwood<br>Commons-Barn Building Oakridge,<br>MD 21900
    <span class="and">And</span>
    4412 Meadow Court Suite B Ridgefield,<br>MD 21950
  </div>
  <div class="like"><i></i>Like us on Friendbook</div>
</section>

<footer class="footer abs"></footer>
<div class="tagline abs">A fun, friendly, and effective place for you to shed serious fat, build tight lean muscle, and have the time of your life doing it.<br>So...what are you waiting for? Register now and try us out RISK FREE!</div>
<div class="foot-links abs">Home<span>|</span>Join Now<span>|</span>About Us<span>|</span>Contact Us<span>|</span>Terms of use</div>
<div class="copy abs">Copyright © 2014 Pinebrook Fit Camp<br>Tern of Services |&nbsp; All Right Reserved</div>
<div class="connect abs"><span class="lbl">CONNECT US</span><i style="background:#3c5aa0"></i><i style="background:#2aa9d8"></i><i style="background:#d8452c"></i></div>
</body>
</html>
```